New Design for our Velintor Gran Reserva Brandy, it is the label design for the bottle label

We need a new bottle label for our Brandy Gran Reserva that we want to bring to the market.

Please have a look at all our current bottles and labels and the feel of our company under www.velintor-example.ch

The bottle that we will be using for the brand is a different one than the one that we already have, the design of the bottle is attached with a document.

I have also attached a briefing in regards to Brandy in general for your information.

### 1. What is Brandy?
Brandy is a distilled spirit made from fermented wine or other fruit wines. It is traditionally aged in oak barrels, which gives it its characteristic color and rich flavor. The aging process in oak is essential for developing the aromas and quality of the brandy.

### 2. What is Brandy Reserva?
A Brandy labeled as "Reserva" has undergone a longer aging process, typically at least 2 to 3 years, in oak barrels. This aging gives the brandy a deeper, more complex flavor profile and a darker color. "Reserva" is often an indication of higher quality.

### 3. Who enjoys drinking Brandy?
Brandy is typically favored by those who appreciate a deep, rich tasting experience. This often includes older consumers who value the time-aged complexity of the spirit. However, Brandy is also gaining popularity among younger people, especially through cocktails and modern serving styles.

### 4. Why is Brandy trending?
Brandy is experiencing a resurgence as consumers increasingly value quality and artisanal production methods. Its versatility in cocktails and association with traditional, luxurious experiences have also contributed to its renewed popularity.

### 5. What colors would be associated with Brandy?
The typical colors associated with Brandy are warm gold, amber, and deep golden-brown tones. These colors reflect the aging process in oak barrels and the richness of the flavors. Other associated colors might include dark brown and mahogany.

### 6. What is important to customers when buying Brandy?
Customers care about the origin of the Brandy, the aging time, the quality of the ingredients, the production method, and the brand. They also pay attention to the prestige of the product and the authenticity of the production.

### 7. What is not important to customers when buying Brandy?
For many customers, the price and packaging (unless it’s especially exclusive) may be less important than the quality and taste of the Brandy. The distillery name might be less significant if it isn’t tied to a particular reputation.

### 8. What do customers know about Swiss Brandy?
Swiss Brandy is still relatively unknown in many markets, but customers who are familiar with it appreciate the precision and quality of Swiss production. Swiss Brandy is assumed to be made with care and under strict quality standards.

### 9. What is Brandy Gran Reserva?
**Brandy Gran Reserva** is an even higher quality and longer-aged version of Brandy. Generally, a Gran Reserva is aged for at least 5 to 10 years or more in oak barrels. This extended aging process gives the Brandy an especially deep, complex flavor profile and often a darker, richer color. Gran Reserva is often regarded as the top-tier product within a Brandy range and appeals to discerning consumers who value quality, refinement, and a luxurious tasting experience.

The label “Gran Reserva” thus indicates the highest quality level for Brandies, similar to other spirits (like wine or whisky), where the aging time is a critical factor.

### 10. What emotions are associated with Brandy?
Brandy is often associated with luxury, relaxation, and comfort. It evokes feelings of tradition, elegance, and sophistication. Drinking Brandy is frequently seen as a moment of reflection and enjoyment.

### 11. How should Brandy be marketed?
Brandy should be marketed with a focus on its artisanal production, quality, and tradition. A narrative around the product, its aging, and origin can help create an emotional connection with the customer. The marketing should also emphasize the versatility of Brandy, whether consumed neat or in cocktails.

### 12. Sales test and label design for Velintor Brandy
For a sales test, I would suggest a tasting in an upscale setting, perhaps paired with a storytelling presentation highlighting the history of the 6-year aged Brandy and its aging in oak barrels.

**Label design**:
The label should reflect the exclusivity of the product, with an elegant, minimalist design. Colors like deep gold, mahogany, and a hint of deep blue could be used to emphasize the aging and quality of the Brandy. The label should include information about the aging time, the use of oak barrels, and a brief story about the Brandy’s production. A seal or embossing highlighting the craftsmanship would also be fitting.

Target Market(s)

Customers that like Brandy

Requirements
Must have
• the Alcohol % must be included on the label as well as our address.

```html
<!DOCTYPE html>
<html lang="en">
<head>
<meta charset="utf-8">
<title>Velintor Brandy Gran Reserva – Label</title>
<link href="https://fonts.googleapis.com/css2?family=Libre+Baskerville:wght@400;700&family=Nunito:wght@400&family=Reenie+Beanie&display=swap" rel="stylesheet">
<style>
  :root {
    --bg: #e9e4dc;
    --panel: #0b0b0b;
    --gold: #b9a05a;
    --gold-dark: #7d6a35;
    --copper: #c2641c;
    --card: #f3eee2;
    --ink: #1b1b1b;
    --rule: #8a8577;
    --flag-red: #d8262c;
    --white: #ffffff;
  }
  * { margin: 0; padding: 0; box-sizing: border-box; }
  html, body { width: 1200px; height: 1200px; overflow: hidden; background: var(--bg); }

  .canvas { position: relative; width: 1200px; height: 1200px; }

  .label {
    position: absolute; left: 385px; top: 30px;
    width: 430px; height: 1140px;
    background: var(--panel);
    border-radius: 215px 215px 4px 4px;
  }
  .label-frame {
    position: absolute; inset: 12px;
    border-radius: 203px 203px 3px 3px;
    border: 12px solid var(--gold-dark);
    outline: 2px solid var(--gold);
    outline-offset: 2px;
  }
  .label-frame::after {
    content: ""; position: absolute; inset: 2px;
    border-radius: 189px 189px 2px 2px;
    border: 2px solid var(--gold);
  }
  .label-body { position: absolute; inset: 0; }

  .swiss-flag { position: absolute; left: 190px; top: 41px; width: 50px; height: 50px; }

  .brand-name {
    position: absolute; top: 124px; left: 0; right: 0; text-align: center;
    font-family: "Libre Baskerville", serif; font-weight: 400;
    font-size: 44px; line-height: 1; color: var(--gold);
  }
  .brand-sub {
    position: absolute; top: 174px; left: 0; right: 0; text-align: center;
    font-family: "Libre Baskerville", serif; font-weight: 700;
    font-size: 17px; line-height: 21px; letter-spacing: 1px; color: var(--gold);
  }

  .product-type {
    position: absolute; left: calc(50% + 8px); top: 572px;
    transform: translate(-50%, -50%) rotate(-90deg) scaleX(0.89);
    font-family: "Libre Baskerville", serif; font-weight: 400;
    font-size: 156px; line-height: 1; color: var(--copper);
    white-space: nowrap; letter-spacing: -2px;
  }

  .grade {
    position: absolute; top: 899px; left: 0; right: 0; text-align: center;
    font-family: "Libre Baskerville", serif; font-size: 33px; line-height: 1.2; color: var(--gold);
  }

  .details {
    position: absolute; left: 56px; top: 948px; width: 320px;
    background: var(--card); border: 1.5px solid var(--rule);
  }
  .details-row { display: flex; height: 50px; }
  .details-row + .details-row { border-top: 1.5px solid var(--rule); }
  .cell {
    display: flex; align-items: center; padding: 0 10px;
    font-family: "Nunito", sans-serif; font-size: 15px; color: var(--ink);
    white-space: nowrap;
  }
  .cell + .cell { border-left: 1.5px solid var(--rule); }
  .age-field { width: 194px; }
  .age-entry { flex: 1; }
  .bottle-field { width: 104px; }
  .bottle-entry { width: 138px; justify-content: center; }
  .bottle-blank { flex: 1; }
  .entry { font-family: "Reenie Beanie", cursive; font-size: 32px; }

  .volume-row {
    position: absolute; left: 56px; right: 54px; top: 1063px; height: 40px;
    display: flex; align-items: center;
    font-family: "Libre Baskerville", serif; font-size: 21px; color: var(--card);
  }
  .volume { width: 153px; }
  .abv-box {
    background: var(--card); color: var(--ink); width: 81px; height: 38px;
    display: flex; align-items: center; justify-content: center;
    font-family: "Reenie Beanie", cursive; font-size: 32px; margin-right: 8px;
  }
</style>
</head>
<body>
<main class="canvas">
  <section class="label" aria-label="Velintor Brandy Gran Reserva bottle label">
    <div class="label-frame"></div>
    <div class="label-body">
      <svg class="swiss-flag" viewBox="0 0 32 32" aria-label="Swiss flag">
        <rect width="32" height="32" fill="var(--flag-red)"/>
        <rect x="13" y="6" width="6" height="20" fill="var(--white)"/>
        <rect x="6" y="13" width="20" height="6" fill="var(--white)"/>
      </svg>
      <div class="brand-name">Velintor</div>
      <div class="brand-sub">SWISS<br>DISTILLERY</div>
      <h1 class="product-type">BRANDY</h1>
      <p class="grade">GRAN RESERVA</p>
      <div class="details">
        <div class="details-row">
          <span class="cell age-field">Aged in oak barrels</span>
          <span class="cell age-entry entry">6 years</span>
        </div>
        <div class="details-row">
          <span class="cell bottle-field">Bottle No</span>
          <span class="cell bottle-entry entry">1/706</span>
          <span class="cell bottle-blank"></span>
        </div>
      </div>
      <div class="volume-row">
        <span class="volume">70 CL</span>
        <span class="abv-box">54.8</span>
        <span class="abv-unit">% VOL.</span>
      </div>
    </div>
  </section>
</main>
</body>
</html>
```